Flyer-Design für Leben am See
Zielgruppe
Der Betrieb vermietet Wohnungen in einer Appartementanlage und Stellplätze für Wohnwägen (in Zukunft Wohncubes) auf einem Campingplatz, wobei die Mieter langfristig bleiben (ab 1 Jahr und länger). Touristen, die kurz- bis mittelfristig einen Wohnwagen/-cube (1 bis 4 Wochen) mieten, sind die Ausnahme. Singles, Paare oder Familien sind die Zielgruppen. Da der Betrieb direkt am See liegt, besteht für Kunden die Möglichkeit, Badekabinen und private Badeplätze anzumieten. Mehr Information unter www.birkenmoos.at
Aufgabenstellung
Das Ziel ist natürlich, die Objekte so attraktiv wie möglich zu präsentieren, und bei den Betrachtern ein positives Gefühl hervorzurufen. Neben den Koordinaten des Betriebes (Lage, Tel, email, etc) soll die Einmaligkeit des Lebens am See in der Anlage dargestellt werden. Es sollen starke Emotionen wie Wärme, Heim, Garten, See, Angekommen sein, ankern und privat zur Ruhe gekommen sein, provoziert werden.

```html
<!DOCTYPE html>
<html lang="de">
<head>
<meta charset="utf-8">
<title>Birkenmoos – Leben und Urlaub am See</title>
<link href="https://fonts.googleapis.com/css2?family=Open+Sans:wght@400;600;700&family=Yanone+Kaffeesatz:wght@400;500;600&display=swap" rel="stylesheet">
<style>
  :root{
    --green:#2f6a3e;
    --green-dark:#23542f;
    --headline:#ecebaa;
    --paper:#ffffff;
    --inner-bg-top:#e9eef6;
    --inner-bg-bottom:#d2dcec;
    --ink:#2a2f36;
    --stage:#cfcfcf;
  }
  *{box-sizing:border-box;margin:0;padding:0}
  html,body{width:1200px;height:1200px;overflow:hidden}
  body{background:var(--stage);font-family:"Open Sans",sans-serif;color:var(--ink);position:relative}
  .spread{position:absolute;left:60px;width:1080px;height:540px;display:flex;box-shadow:0 4px 14px rgba(0,0,0,.18)}
  .spread--outer{top:40px}
  .spread--inner{top:620px;flex-direction:column;background:linear-gradient(180deg,var(--inner-bg-top),var(--inner-bg-bottom))}

  /* back page */
  .back{width:540px;height:540px;background:var(--green);position:relative;color:#e6efe8}
  .back__contact{position:absolute;left:50px;bottom:32px;font-size:11px;line-height:1.45}
  .back__contact p{margin-bottom:12px}
  .back__contact p:last-child{margin-bottom:0}

  /* title page */
  .cover{width:540px;height:540px;background:var(--paper);position:relative}
  .cover__brand{position:absolute;top:38px;left:0;right:0;display:flex;flex-direction:column;align-items:center;gap:10px}
  .cover__mark{width:60px;height:60px;background:var(--green)}
  .cover__name{font-family:"Open Sans",sans-serif;font-weight:700;font-size:19px;letter-spacing:1.5px;color:var(--green);text-transform:uppercase}
  .cover__rule{position:absolute;top:146px;left:0;right:0;height:4px;background:var(--green)}
  .cover__photo{position:absolute;top:152px;left:0;right:0;height:360px;
    background:linear-gradient(180deg,#c9d4dc 0%,#8fa3ab 35%,#6d6a58 70%,#a98e70 100%)}
  .cover__headline{position:absolute;right:40px;top:290px;font-family:"Yanone Kaffeesatz",sans-serif;font-weight:500;color:var(--headline);line-height:.82;text-align:right;text-shadow:0 1px 2px rgba(0,0,0,.35)}
  .cover__headline .big{font-size:70px}
  .cover__headline .small{font-size:34px}
  .cover__line1{display:block;margin-right:70px}
  .cover__band{position:absolute;left:0;right:0;bottom:0;height:28px;background:var(--green)}

  /* inner spread */
  .photos{display:flex;height:225px}
  .photo{height:100%}
  .photo--lake{width:385px;background:linear-gradient(180deg,#cfd9e6 0%,#7f9a5e 30%,#9fb0c8 55%,#6b7d52 100%)}
  .photo--meadow{width:155px;background:linear-gradient(160deg,#b7c4a5 0%,#4e6b2d 50%,#5d4a7d 100%)}
  .photo--cabin{width:159px;background:linear-gradient(180deg,#d9cdb6 0%,#a08660 55%,#7d6a4b 100%)}
  .photo--jetty{width:381px;background:linear-gradient(180deg,#dfe7f0 0%,#6f9a52 25%,#a4b8c8 45%,#8da3b3 80%,#9a8468 100%)}
  .columns{position:relative;flex:1;display:grid;grid-template-columns:270px 270px 270px 270px;padding:20px 0 0}
  .col{padding:0 18px 0 32px;font-size:10px;line-height:1.5}
  .col--first{padding-left:32px;padding-right:12px}
  .col--second{padding-left:10px;padding-right:26px}
  .col h2{font-family:"Yanone Kaffeesatz",sans-serif;font-weight:500;font-size:27px;color:var(--green);margin-bottom:10px;line-height:1}
  .col p + p{margin-top:12px}
  .col--second p{margin-top:37px}
  .info{position:absolute;left:32px;bottom:46px;width:480px;font-size:13px;font-weight:600;color:var(--green-dark);line-height:1.45}
</style>
</head>
<body>

<section class="spread spread--outer">
  <div class="back">
    <div class="back__contact">
      <p>Birkenmoos Betriebs GmbH</p>
      <p>Birkenmoos 12<br>4861 Seeberg<br>Tel: +43 7662 5140</p>
      <p>info@birkenmoos.at<br>www.birkenmoos.at</p>
    </div>
  </div>
  <div class="cover">
    <div class="cover__brand">
      <div class="cover__mark"></div>
      <div class="cover__name">Birkenmoos</div>
    </div>
    <div class="cover__rule"></div>
    <div class="cover__photo" role="img" aria-label="Familie sitzt auf einem Holzsteg am See und spritzt mit Wasser"></div>
    <h1 class="cover__headline">
      <span class="cover__line1 big">Leben</span>
      <span class="small">und</span> <span class="big">Urlaub</span><br>
      <span class="small">am</span> <span class="big">See</span>
    </h1>
    <div class="cover__band"></div>
  </div>
</section>

<section class="spread spread--inner">
  <div class="photos">
    <div class="photo photo--lake" role="img" aria-label="Seeufer mit Schilf und grünen Hügeln"></div>
    <div class="photo photo--meadow" role="img" aria-label="Wiese mit Liegestuhl und Pflanzen"></div>
    <div class="photo photo--cabin" role="img" aria-label="Holzwand einer Badekabine"></div>
    <div class="photo photo--jetty" role="img" aria-label="Badesteg mit Leiter im ruhigen See"></div>
  </div>
  <div class="columns">
    <div class="col col--first">
      <h2>Appartements</h2>
      <p>Wenn Sie eine gemütliche Atmosphäre mit Blick auf den Irrsee oder Dachstein suchen, dann finden Sie bei uns die richtige Wohnung. Die Wohnungen haben 2 Zimmer samt Nebenräume und sind mit Küche, Bad und Kabel TV ausgestattet. Jede Wohnung verfügt über einen Parkplatz. Ein Badeplatz direkt am See</p>
    </div>
    <div class="col col--second">
      <p>kann mitbenützt werden. Es besteht auch die Möglichkeit, einen privaten Badeplatz mit exklusiven Seezugang mit zu mieten. Fischer oder Bootsbesitzer können sich einen eigenen Platz am See mieten. Der Hof liegt verkehrstechnisch optimal zwischen der Westbahn (5 Min.) und der Westautobahn (10 Min.)</p>
    </div>
    <div class="col">
      <h2>Camping</h2>
      <p>Die großzügigen Plätze für Wohnwägen und Zelte liegen direkt am See. Für Familien und Fischer der ideale Platz, wo man entspannen und leben kann. Wasser, Abwasser, Strom und TV sind bei jedem einzelnen Platz installiert. Zusätzlich können ein Bootsliegeplatz, privater Badeplatz und Kabine mit gemietet werden. Zwei großzügige und gepflegte Badeplätze stehen den Familien zur Verfügung. Abhängig von der Kombination unseres Angebotes und Ihren Wünschen machen wir ein Anbot auf Anfrage.</p>
    </div>
    <div class="col">
      <h2>Kabinen und Badeplätze</h2>
      <p>Die sommerlichen Badefreuden ergänzt eine private Kabine, wo alle Badesachen verstaut werden können. Unsere neuen Kabinen sind mit Strom, Licht und – falls gewünscht – mit Wasser ausgestattet. Die Kabinen können in Kombination mit einem privaten Badeplatz mit eigenen Einstieg in den See kombiniert werden.</p>
      <p>In dieser gepflegten Privatatmosphäre lässt sich die Sommerfrische angenehm in Ruhe genießen. Reservieren Sie sich einen Platz in der ersten Reihe direkt am See.</p>
    </div>
    <p class="info">Für Information über die verschiedenen Pakete nutzen Sie das Kontaktformular auf unserer Webseite oder rufen Sie uns an.</p>
  </div>
</section>

</body>
</html>
```